Harbor Learning Center Posters Showing Building Blocks

We need poster designs for a School in Arizona for kids with Autism. There will be 4 such posters needed which highlight our schools building blocks. Requirements for all 4 posters are as followed: 1) We need the Harbor Learning Center Logo on each poster. I have included attachment. 2) The posters need the following titles: Building Block #1 (for the first poster), Building Block #2 for the 2nd poster, Building Block #3 for the 3rd poster, and Building Block #4 for the forth poster. 3) The main text and focus of the posters will be the following key words: For the first poster the words "Kids first in every decision". The words for the second poster are: "Students are friends with each other, and welcome new students with open arms." The words for the 3rd poster are: "The school is quiet, and students are working hard to do their best." The words for the 4th poster are: "Parents see amazing improvement in their child." 4) We would love to use some of the kids art from our schools if possible. Use your expertise to decide. I will send these out as well. 5) Try and design the posters around the key words from each poster 6) I am sure if landscape or portrait would be best so I will let the experts decide. All 4 posters need to be the same layout once decided.

Target Market(s)

These posters are for the school only. Prospective students/parents will see these posters so they will be used for Marketing from that perspective. We may put out into local community in future.

Industry/Entity Type

School

Font styles to use
Serif

Requirements
Must have
• 1) Logo (Harbor Learning Center for Growth and Discovery)
• 2) Title: as described in write up
• 3) Key words: as described in write up
Nice to have
• Kids art from school. Note: This is the first time that I have been on this site so I may have made a mistake by putting 4 posters on one project. I am assuming that I would need to pay more to have 4 posters so let me know if I need to modify the project in any way?

```html
<!DOCTYPE html>
<html lang="en">
<head>
<meta charset="utf-8">
<title>School Building Block #4 – Harbor Learning Center</title>
<link rel="stylesheet" href="https://fonts.googleapis.com/css2?family=Alegreya+SC:wght@700&family=Gochi+Hand&family=Crimson+Text:wght@600&display=swap">
<style>
  :root {
    --paper: #ffffff;
    --lime: #d6e02a;
    --orange: #f26a2e;
    --orange-box: #ef6a2f;
    --pale-lime: #f2f0a6;
    --blob: #e6e7e8;
    --silhouette: #ffffff;
    --ink: #1a1a1a;
    --brand: #1a1a1a;
    --square: #e63946;
  }
  * { margin: 0; padding: 0; box-sizing: border-box; }
  html, body { width: 848px; height: 1200px; overflow: hidden; background: var(--paper); }
  .poster { position: relative; width: 848px; height: 1200px; background: var(--paper); overflow: hidden; }

  .title-banner {
    position: absolute; left: 70px; top: 26px; width: 712px; height: 130px;
    background: var(--lime);
    clip-path: polygon(0 2%, 35% 0, 70% 3%, 100% 0, 99% 50%, 100% 100%, 60% 97%, 25% 100%, 1% 98%, 0 50%);
    display: flex; justify-content: center; padding-top: 20px;
  }
  .title-banner h1 {
    font-family: "Alegreya SC", Georgia, serif; font-weight: 700;
    font-size: 66px; letter-spacing: 1px; color: var(--orange); line-height: 1;
  }
  .block-tag {
    position: absolute; left: 305px; top: 137px; width: 226px; height: 69px;
    background: var(--orange-box);
    box-shadow: 2px 3px 4px rgba(0,0,0,.25);
    display: flex; align-items: center; justify-content: center;
    font-family: "Alegreya SC", Georgia, serif; font-weight: 700;
    font-size: 38px; color: var(--pale-lime);
  }

  .backdrop { position: absolute; left: 0; top: 0; width: 848px; height: 1200px; }

  .kids-silhouettes {
    position: absolute; left: 100px; top: 300px; width: 410px; height: 390px;
    background: var(--silhouette); border-radius: 46% 46% 30% 30%;
  }
  .kids-art {
    position: absolute; left: 315px; top: 325px; width: 495px; height: 565px;
    clip-path: polygon(0 0, 100% 0, 100% 100%, 205px 100%, 205px 42%, 0 42%);
    background: linear-gradient(160deg, #3f8f3a 0%, #5b6fc9 35%, #e2622f 60%, #2f7a3a 85%, #6b4a2f 100%);
  }

  .key-message {
    position: absolute; left: 82px; top: 612px; z-index: 2;
    font-family: "Gochi Hand", "Comic Sans MS", cursive;
    color: var(--ink); transform: rotate(-4deg); transform-origin: left top;
    line-height: 1;
  }
  .key-message span { display: block; white-space: nowrap; }
  .line-1 { font-size: 72px; }
  .line-2 { font-size: 48px; margin: 4px 0 0 80px; }
  .line-2 em, .line-4 em { font-style: normal; font-size: 64px; }
  .line-3 { font-size: 56px; margin: 4px 0 0 20px; }
  .line-4 { font-size: 48px; margin: 2px 0 0 44px; }

  .brand {
    position: absolute; left: 282px; top: 1048px;
    display: flex; align-items: center; gap: 10px;
  }
  .brand-square { width: 44px; height: 44px; background: var(--square); }
  .brand-name {
    font-family: "Crimson Text", Georgia, serif; font-weight: 600;
    color: var(--brand); font-size: 19px; line-height: 1.15;
  }
</style>
</head>
<body>
<main class="poster">
  <svg class="backdrop" viewBox="0 0 848 1200" aria-hidden="true">
    <path fill="var(--blob)" d="M90 470 C60 360 170 280 300 285 C430 290 560 265 680 300 C780 340 820 450 800 600 C790 740 760 880 640 960 C520 1020 330 1010 210 950 C100 890 40 760 55 640 C60 570 100 520 90 470 Z"/>
  </svg>

  <div class="title-banner"><h1>School Building</h1></div>
  <div class="block-tag">Block #4</div>

  <div class="kids-silhouettes" role="img" aria-label="White silhouettes of two children holding hands"></div>
  <div class="kids-art" role="img" aria-label="Child figure cut out of colourful student painting, arms outstretched"></div>

  <p class="key-message">
    <span class="line-1">Parents</span>
    <span class="line-2">see <em>amazing</em></span>
    <span class="line-3">improvement</span>
    <span class="line-4">in their <em>child!</em></span>
  </p>

  <div class="brand">
    <div class="brand-square"></div>
    <div class="brand-name">HARBOR LEARNING CENTER<br>for Growth and Discovery</div>
  </div>
</main>
</body>
</html>
```